PowerPoint Template - Korvel Mint

You find in the attached file a short description of our firm, logo, mission, vision and values. We made an empty template in order to let you free to imagine. We-have high expectations on ideas "out of the box" to merge our job (consulting firm) with Zen concept. We really Would like "Zen" look and feel, to show our difference. And we want to avoid "standard consulting" (smart guys with ties, shaking hand with Brimlo smilies ...) Thank you

Target Market(s)

organization (Rather big ones)

Industry/Entity Type

Consulting

Number of Pages Required

3 page

Font styles to use
Sans Serif

Requirements
Must have
• - Some nice pictures - Be really "Zen" (quiet, smart, luxury, people centric)
Should not have
• really looks like "standard consulting" (smart guys with ties, shaking hand with Brimlo smilies ...)

```html
<!DOCTYPE html>
<html lang="en">
<head>
<meta charset="utf-8">
<title>Name Explanation – Korvel Mint</title>
<link href="https://fonts.googleapis.com/css2?family=Lato:wght@400;700;900&display=swap" rel="stylesheet">
<style>
  :root {
    --accent: #e8601c;
    --ink: #2b2b2b;
    --body: #333333;
    --ghost: #efefef;
    --paper: #ffffff;
  }
  html, body {
    margin: 0;
    padding: 0;
    overflow: hidden;
    background: var(--paper);
  }
  .slide {
    position: relative;
    width: 1200px;
    height: 694px;
    overflow: hidden;
    background: var(--paper);
    font-family: "Lato", sans-serif;
  }
  .slide__edge {
    position: absolute;
    left: 0;
    top: 0;
    width: 5px;
    height: 100%;
    background: var(--accent);
  }
  .slide__title {
    position: absolute;
    left: 64px;
    top: 58px;
    margin: 0;
    font-size: 37px;
    font-weight: 900;
    color: var(--accent);
    letter-spacing: -0.3px;
  }
  .backdrop-name {
    position: absolute;
    left: 0;
    top: 0;
  }
  .diagram {
    position: absolute;
    left: 0;
    top: 0;
  }
  .brand-name {
    position: absolute;
    left: 0;
    width: 1204px;
    top: 252px;
    margin: 0;
    text-align: center;
    font-size: 40px;
    font-weight: 700;
    letter-spacing: 0.42em;
    color: var(--ink);
  }
  .pillar {
    position: absolute;
    top: 362px;
    width: 157px;
    height: 157px;
    box-sizing: border-box;
    margin: 0;
    padding: 0;
    list-style: none;
    text-align: center;
    font-size: 13px;
    line-height: 28px;
    color: var(--body);
  }
  .pillar--calm { left: 346px; padding-top: 18px; }
  .pillar--value { left: 694px; padding-top: 5px; }
</style>
</head>
<body>
<div class="slide">
  <div class="slide__edge"></div>

  <svg class="backdrop-name" width="1200" height="694" aria-hidden="true">
    <text x="156" y="596" textLength="900" lengthAdjust="spacing"
          font-family="Lato, sans-serif" font-size="84" font-weight="700"
          fill="var(--ghost)">KORVEL MINT</text>
  </svg>

  <h1 class="slide__title">NAME EXPLANATION</h1>

  <p class="brand-name">KORVEL MINT</p>

  <svg class="diagram" width="1200" height="694" aria-hidden="true">
    <g fill="none" stroke="var(--accent)" stroke-width="1" stroke-dasharray="5 3">
      <polyline points="422,362 584,322 752,362"/>
      <rect x="346.5" y="362.5" width="156" height="156" rx="4"/>
      <rect x="694.5" y="362.5" width="156" height="156" rx="4"/>
    </g>
  </svg>

  <ul class="pillar pillar--calm">
    <li>No stress</li>
    <li>Respect</li>
    <li>Human centric</li>
    <li>Accept mistakes</li>
  </ul>

  <ul class="pillar pillar--value">
    <li>Value for customers</li>
    <li>and for ourselves</li>
    <li>Value by action</li>
    <li>Quick Value</li>
    <li>Measurable value</li>
  </ul>
</div>
</body>
</html>
```